Dental Office needs Dynamic Wordpress Website Design

We need a a dynamic WordPress website design including SEO. We also need a mobile site. We would like the design to be easy to navigate, simple and modern. We would like to stick with a black, white and purple theme and existing logo and font. We have content and professional photos all ready to go as we would like to proceed asap.

Industry/Entity Type

Dental

```html
<!DOCTYPE html>
<html lang="en">
<head>
<meta charset="utf-8">
<title>Maple Crest Dental</title>
<link href="https://fonts.googleapis.com/css2?family=Open+Sans:wght@300;400;600;700&display=swap" rel="stylesheet">
<style>
:root{
  --purple:#6b1466;
  --purple-dark:#4e0c4b;
  --purple-soft:#8a4f8a;
  --ink:#222;
  --muted:#666;
  --page:#f4f4f4;
  --band-top:#ffffff;
  --band-bottom:#d9d9d9;
  --footer:#ebebeb;
}
*{box-sizing:border-box;margin:0;padding:0}
html,body{width:1095px;height:1200px;overflow:hidden}
body{position:relative;background:var(--page);font-family:'Open Sans',sans-serif;color:var(--ink)}
.top-band{position:absolute;left:0;top:0;width:1095px;height:382px;background:linear-gradient(var(--band-top),var(--band-bottom))}
.brand{position:absolute;left:128px;top:13px;width:196px;height:91px;background:#fff;display:flex;align-items:center;gap:10px;padding-left:24px}
.brand-mark{width:22px;height:22px;background:var(--purple)}
.brand-name{font-size:19px;font-weight:400;color:var(--purple);line-height:1.1}
.phone{position:absolute;right:152px;top:64px;font-size:27px;font-weight:300;color:#444;display:flex;align-items:center;gap:6px}
.nav{position:absolute;left:152px;top:104px;width:791px;height:48px;background:linear-gradient(var(--purple),var(--purple-dark))}
.nav a{position:absolute;top:15px;color:#fff;font-size:12.5px;font-weight:700;text-decoration:none}
.search{position:absolute;left:562px;top:10px;width:219px;height:27px;background:var(--purple-dark);border-radius:2px;color:#a87ba6;font-size:10px;padding:7px 9px}
.hero{position:absolute;left:152px;top:152px;width:791px;height:304px;background:linear-gradient(100deg,#e9e4e0 0%,#c9d8d6 45%,#9fb6b4 70%,#d8d4d0 100%)}
.hero-caption{position:absolute;left:471px;top:74px;width:293px;height:187px;background:rgba(70,70,70,.82);padding:14px 18px;color:#fff;font-size:12px;font-weight:300;line-height:20px}
.btn{position:absolute;left:63px;top:144px;width:167px;height:31px;background:linear-gradient(#8a4f8a,#6b1466);border:1px solid #b58bb3;color:#fff;font-size:13px;font-weight:600;text-align:center;line-height:29px}
.dots{position:absolute;left:21px;top:273px;display:flex;gap:4px}
.dots span{width:13px;height:13px;border-radius:50%;background:#fff}
.dots span.on{background:var(--purple)}
h2{position:absolute;font-size:20px;font-weight:400;color:#111}
.welcome-photo{position:absolute;left:154px;top:520px;width:451px;height:165px;background:linear-gradient(90deg,#d9b79e,#e8e3de 55%,#cfd9e0)}
.copy{position:absolute;font-size:12px;color:var(--muted);line-height:20.3px;font-weight:400}
.avatar{position:absolute;left:625px;top:537px;width:84px;height:86px;border:2px solid var(--purple-soft);background:linear-gradient(#7c8a6a,#c99a84)}
.doc-name{position:absolute;left:719px;top:557px;font-size:21px;font-weight:400}
.doc-role{position:absolute;left:719px;top:588px;font-size:11.5px}
.partners{position:absolute;left:156px;top:905px;width:787px;height:42px;display:flex;justify-content:space-between;align-items:center}
.partners span{height:26px;width:90px;background:#c7cbd3;border-radius:3px}
.footer{position:absolute;left:0;top:978px;width:1095px;height:222px;background:linear-gradient(var(--page),#dedede)}
.col{position:absolute;top:22px}
.col h3{font-size:13px;font-weight:700;color:var(--purple);margin-bottom:13px}
.col li{list-style:none;font-size:12px;color:#333;line-height:20.5px}
.col.support li{font-size:13px;line-height:23px}
.org{font-size:13.5px;font-weight:600;color:var(--purple);margin:-3px 0 8px -3px}
.address{font-size:13px;line-height:23px;color:#333}
.map{width:184px;height:100px;background:linear-gradient(135deg,#dfe6d9,#cfd8cc 60%,#e4e0d4)}
.social li{display:flex;align-items:center;gap:10px;font-size:13px;margin-bottom:7px;line-height:26px}
.social i{width:26px;height:26px;border-radius:50%;background:var(--purple);display:block}
.copyright{position:absolute;left:0;width:1095px;top:1156px;text-align:center;font-size:11.5px;color:#222}
</style>
</head>
<body>
<div class="top-band"></div>

<div class="brand"><span class="brand-mark"></span><span class="brand-name">Maple Crest<br>Dental</span></div>
<div class="phone">
  <svg width="18" height="22" viewBox="0 0 18 22"><path d="M4 1l4 5-2 3c1 3 3 6 6 8l3-2 4 4-3 3C9 21 1 12 1 4z" fill="#555"/></svg>
  555-014-2280
</div>

<nav class="nav">
  <a style="left:28px">Home</a>
  <a style="left:90px">About Us</a>
  <a style="left:171px">Services</a>
  <a style="left:247px">FAQ's</a>
  <a style="left:307px">Contact Us</a>
  <div class="search">Search</div>
</nav>

<section class="hero" role="img" aria-label="Photo of a smiling dental assistant with a dentist treating a patient">
  <div class="hero-caption">
    Lorem ipsum dolor sit amet, consectetur adipisicing elit, sed do eiusmod tempor incididunt ut labore et dolore magna aliqua. Ut enim ad minim veniam, quis nostrud exercitation ullamco laboris nisi ut aliquip ex ea commodo consequat.
    <div class="btn">Make An Appointment</div>
  </div>
  <div class="dots"><span class="on"></span><span></span><span></span><span></span><span></span></div>
</section>

<h2 style="left:153px;top:484px">Welcome to Maple Crest Dental</h2>
<div class="welcome-photo" role="img" aria-label="Photo of a patient in the dental chair during a check-up"></div>
<p class="copy" style="left:152px;top:698px;width:456px">Sed ut perspiciatis unde omnis iste natus error sit voluptatem accusantium doloremque laudantium, totam rem aperiam, eaque ipsa quae ab illo inventore verita­tis et quasi architecto beatae vitae dicta sunt explicabo. Nemo enim ipsam volupta­tem quia voluptas sit aspernatur aut odit aut fugit, sed quia consequuntur magni dolores eos qui ratione voluptatem sequi nesciunt. Neque porro quisquam est, qui dolorem ipsum quia dolor sit amet, consectetur, adipisci velit, sed quia non numquam eius modi tempora incidunt ut labore et dolore magnam aliquam quaerat voluptatem. Ut enim ad minima veniam, quis nostrum exercitationem ullam corporis suscipit labo­riosam, nisi ut aliquid ex ea commodi consequat</p>

<h2 style="left:623px;top:484px">About Me</h2>
<div class="avatar" role="img" aria-label="Portrait photo of the practice director"></div>
<div class="doc-name">Dr. Adrian Kowal</div>
<div class="doc-role">Director of Maple Crest Dental</div>
<p class="copy" style="left:632px;top:659px;width:310px">At vero eos et accusamus et iusto odio dignissimos duci­mus qui blanditiis praesentium voluptatum deleniti atque corrupti quos dolores et quas molestias excepturi sint occaecati cupiditate non provident, similique sunt in culpa qui officia deserunt mollitia animi, id est laborum et dolo­rum fuga. Et harum quidem rerum facilis est et expedita distinctio. Nam libero tempore, cum soluta nobis est eligendi optio cumque nihil impedit quo minus id quod maxime placeat facere possimus, omnis voluptas assumenda est, omnis dolor repellendus.</p>

<div class="partners" aria-label="Partner brands">
  <span></span><span style="width:86px"></span><span style="width:84px"></span><span style="width:66px"></span><span style="width:82px"></span><span style="width:94px;background:#2f4f7a"></span><span style="width:102px"></span>
</div>

<footer class="footer">
  <div class="col" style="left:152px">
    <h3>Menu Links</h3>
    <ul><li>Home</li><li>About Us</li><li>Services</li><li>FAQ's</li><li>Contact Us</li></ul>
  </div>
  <div class="col support" style="left:293px">
    <h3>Support Links</h3>
    <ul><li>Terms &amp; Conditions</li><li>Legal Notice</li><li>Privacy Policy</li></ul>
  </div>
  <div class="col" style="left:443px">
    <h3>Contact Us</h3>
    <div class="org">Maple Crest Dental</div>
    <div class="address">1180 Harbor Rd W<br>Fairview,ON A1B 2C3<br>( 555 )&nbsp; 014 -3377</div>
  </div>
  <div class="col" style="left:622px">
    <h3>Location</h3>
    <div class="map" role="img" aria-label="Street map showing the office location"></div>
  </div>
  <div class="col" style="left:830px">
    <h3>Connect With Us</h3>
    <ul class="social"><li><i></i>Chatter</li><li><i></i>Friendbook</li><li><i></i>ProLink</li></ul>
  </div>
</footer>
<div class="copyright">© 2014 Company name ,All Rights Reserved</div>
</body>
</html>
```